Create New Bussiness Card For New Shoes Store

Vandrule is a store that sells a variety of skateboard shoes such as Kestro, Mollen etc. we also sell some skateboard and all skateboard accessories.
we like black and white style logo, but also like blue as well.
We are fully assembled with a deck, truck, wheels, and bearings. Add some personality to your board with a fun, graphic skateboard deck. Constructed of thick 7 ply maple,
Target Market(s)
Target audience: 12-40 year old
especially for young man
Industry/Entity Type
Industrial
Contact Information for Business Card
Name: Vandrule
Address1: 2483 Harlow Brisket Rd
City: Xenia
State: Ohio
Zip: 45385
Country: US
Phone: 614830296
email: markolvenby@plimmail.test

```html
<!DOCTYPE html>
<html lang="en">
<head>
<meta charset="utf-8">
<title>Vandrule Business Card</title>
<link href="https://fonts.googleapis.com/css2?family=Open+Sans:wght@300;400&family=Oswald:wght@500&display=swap" rel="stylesheet">
<style>
  :root {
    --backdrop: #2a2826;
    --card: #1e1e20;
    --card-back: #262728;
    --accent: #c57fd4;
    --emboss: #4a4b4d;
  }
  * { margin: 0; padding: 0; box-sizing: border-box; }
  html, body {
    width: 1200px; height: 716px; overflow: hidden;
    background: var(--backdrop);
  }
  .stage {
    position: relative; width: 1200px; height: 716px;
    display: flex; align-items: center; justify-content: center; gap: 56px;
  }
  .card {
    width: 500px; height: 286px; border-radius: 4px;
    position: relative;
    box-shadow: 0 12px 30px rgba(0,0,0,.45);
  }
  .card-front { background: var(--card); }
  .card-back {
    background: var(--card-back);
    display: flex; align-items: center; justify-content: center;
  }
  .brand {
    position: absolute; left: 46px; top: 50%; transform: translateY(-50%);
    display: flex; align-items: center; gap: 10px;
    font-family: "Open Sans", sans-serif; font-weight: 300;
    font-size: 30px; color: var(--accent); letter-spacing: .5px;
  }
  .brand-dot {
    width: 12px; height: 12px; border-radius: 50%;
    border: 1.5px solid var(--accent);
  }
  .divider {
    position: absolute; left: 238px; top: 52px;
    width: 2px; height: 182px; background: var(--accent);
  }
  .details {
    position: absolute; left: 266px; top: 62px;
    font-family: "Open Sans", sans-serif; color: var(--accent);
  }
  .person-name {
    font-family: "Oswald", sans-serif; font-weight: 500;
    font-size: 21px; letter-spacing: .5px; line-height: 1.1;
  }
  .person-role { font-size: 11px; letter-spacing: .6px; margin-bottom: 14px; }
  .contact-line {
    display: flex; align-items: center; gap: 9px;
    font-size: 11.5px; margin-bottom: 7px;
  }
  .contact-line svg { width: 12px; height: 12px; flex: none; }
  .address { font-size: 11.5px; line-height: 1.55; margin-top: 8px; }
  .brand-back {
    display: flex; align-items: center; gap: 12px;
    font-family: "Open Sans", sans-serif; font-weight: 300;
    font-size: 40px; color: var(--emboss);
  }
  .brand-back .brand-dot { width: 15px; height: 15px; border-color: var(--emboss); }
</style>
</head>
<body>
<main class="stage">
  <section class="card card-front">
    <div class="brand"><span>Vandrule</span><span class="brand-dot"></span></div>
    <div class="divider"></div>
    <div class="details">
      <p class="person-name">DALE CORWIN</p>
      <p class="person-role">DIRECTOR</p>
      <p class="contact-line">
        <svg viewBox="0 0 12 12" aria-hidden="true"><circle cx="6" cy="6" r="5.3" fill="none" stroke="currentColor" stroke-width="1"/><path d="M4 3.5c0 2.5 1.5 4.5 4 5l.7-1-1.3-.8-.6.6c-.9-.4-1.4-1-1.7-1.8l.6-.6-.7-1.4z" fill="currentColor"/></svg>
        061 483 0296
      </p>
      <p class="contact-line">
        <svg viewBox="0 0 12 12" aria-hidden="true"><rect x="0.5" y="2" width="11" height="8" rx="1" fill="currentColor"/><path d="M1 2.5l5 4 5-4" fill="none" stroke="#1e1e20" stroke-width="1"/></svg>
        markolvenby@plimmail.test
      </p>
      <p class="address">2483 Harlow Brisket Rd<br>Thornbury, Calden, 58214, Us</p>
    </div>
  </section>
  <section class="card card-back">
    <div class="brand-back"><span>Vandrule</span><span class="brand-dot"></span></div>
  </section>
</main>
</body>
</html>
```